App Design for a petrol price in Nigeria

Through your already existing prototypes, we intend to design an app that would show petrol prices in Nigeria. The app would enable the user monitor the prices of petrol products in real time from nearby stations.

Industry/Entity Type

Gas And Oil

Requirements
Must have
• User community (sign up) and crowdsourced database integration

```html
<!DOCTYPE html>
<html lang="en">
<head>
<meta charset="utf-8">
<title>PumpWatch NG – App Screens</title>
<link href="https://fonts.googleapis.com/css2?family=Roboto:wght@400;500;700&family=Signika:wght@500&display=swap" rel="stylesheet">
<style>
:root{
  --teal:#03c1ae;
  --teal-dark:#0f5f55;
  --white:#ffffff;
  --paper:#f1f1f1;
  --ink:#333333;
  --muted:#9a9a9a;
  --line:#e4e4e4;
  --map:#ececec;
  --pin:#f7d21b;
  --dim:#6b6b6b;
}
*{box-sizing:border-box;margin:0;padding:0}
html,body{width:952px;height:1200px;overflow:hidden}
body{background:var(--teal);font-family:"Roboto",sans-serif;color:var(--ink);position:relative}
.screen{position:absolute;width:243px;height:498px;border-radius:22px;overflow:hidden;background:var(--white)}
.screen--splash{left:59px;top:53px;background:var(--teal)}
.screen--signin{left:353px;top:53px;background:var(--paper)}
.screen--stations{left:647px;top:53px}
.screen--filter{left:206px;top:625px;background:var(--dim)}
.screen--notify{left:500px;top:625px}
.abs{position:absolute}

/* splash */
.brand-mark{position:absolute;width:64px;height:71px;background:var(--white);border-radius:5px}
.splash-mark{left:89px;top:191px}
.brand-name{position:absolute;left:0;right:0;top:279px;text-align:center;font-family:"Signika",sans-serif;font-weight:500;font-size:22px;color:var(--white);letter-spacing:-.3px}

/* sign in */
.signin-mark{left:89px;top:70px;width:64px;height:71px;box-shadow:0 2px 6px rgba(0,0,0,.05)}
.pill{position:absolute;left:35px;width:173px;height:32px;border-radius:16px;display:flex;align-items:center;font-size:10px}
.pill--social{background:var(--white);border:1px solid var(--teal);justify-content:center;color:var(--ink)}
.pill--field{background:var(--white);padding:0 20px;color:#bcbcbc;justify-content:space-between}
.pill--primary{background:var(--teal);color:var(--white);justify-content:center;font-weight:500;font-size:9.5px}
.or{position:absolute;left:0;right:0;top:262px;text-align:center;font-size:9px;font-weight:500}
.forgot{position:absolute;left:0;right:0;top:412px;text-align:center;font-size:9px;color:var(--teal);font-weight:500}
.signup{position:absolute;left:0;right:0;top:450px;text-align:center;font-size:9.5px}
.signup b{color:var(--teal);font-size:11px}

/* app header */
.app-bar{position:absolute;left:0;top:0;width:100%;height:63px;background:var(--teal)}
.app-bar__title{position:absolute;left:0;right:0;top:38px;text-align:center;color:var(--white);font-weight:700;font-size:11.5px}
.app-bar__menu{position:absolute;left:18px;top:41px}
.avatar{position:absolute;left:207px;top:33px;width:26px;height:26px;border-radius:50%;background:linear-gradient(#6a4a3a,#3a2a22);border:2px solid var(--white)}

/* stations */
.map{position:absolute;left:0;top:63px;width:100%;height:395px;background:linear-gradient(160deg,#f2f2f2,#e6e6e6)}
.search{position:absolute;left:13px;top:185px;width:155px;height:31px;border-radius:16px;background:var(--white);box-shadow:0 2px 6px rgba(0,0,0,.06);display:flex;align-items:center;padding-left:10px;gap:5px;font-size:8.5px;color:#c2c2c2}
.filter-btn{position:absolute;left:178px;top:185px;width:51px;height:31px;border-radius:16px;background:var(--white);box-shadow:0 2px 6px rgba(0,0,0,.06);color:var(--teal);font-weight:500;font-size:9px;display:flex;align-items:center;justify-content:center}
.station-card{position:absolute;left:13px;top:229px;width:216px;height:217px;background:var(--white);border-radius:6px;overflow:hidden;box-shadow:0 2px 8px rgba(0,0,0,.08)}
.station-card__head{height:27px;background:var(--teal);color:var(--white);font-weight:700;font-size:8.5px;position:relative}
.station-card__head span{position:absolute;top:9px}
.station-row{position:relative;height:26.5px;margin:0 28px 0 11px;border-bottom:1px solid var(--line);font-size:9px}
.station-row:last-child{border-bottom:none}
.station-row .price{position:absolute;left:0;top:8px;color:#777}
.station-row .dot{position:absolute;left:76px;top:6px;width:13px;height:13px;border-radius:50%;background:var(--teal);opacity:.35}
.station-row .name{position:absolute;left:92px;top:8px;color:var(--teal);font-weight:500}
.station-row .dist{position:absolute;right:0;top:8px;color:#666}
.scrollbar{position:absolute;right:10px;top:36px;width:4px;height:171px;border-radius:2px;background:#eee}
.scrollbar i{display:block;width:4px;height:32px;border-radius:2px;background:var(--teal)}

/* nav */
.tab-bar{position:absolute;left:0;bottom:0;width:100%;height:42px;background:var(--white);border-top:1px solid #eee}
.tab{position:absolute;top:8px;transform:translateX(-50%);text-align:center;font-size:6px;color:var(--muted);letter-spacing:.2px}
.tab svg{display:block;margin:0 auto 3px}
.tab--active{color:var(--teal)}

/* filter */
.dim-bar{position:absolute;left:0;top:0;width:100%;height:63px;background:var(--teal-dark)}
.blur-glow{position:absolute;left:145px;top:98px;width:55px;height:55px;border-radius:50%;background:rgba(247,210,27,.35);filter:blur(3px)}
.sheet{position:absolute;left:0;top:163px;width:100%;height:335px;background:var(--white);border-radius:30px 30px 0 0}
.sheet h2{position:absolute;left:28px;font-size:13px;font-weight:500;color:#3a3a3a}
.segment{position:absolute;left:28px;top:48px;width:186px;height:28px;border-radius:14px;background:#ececec;display:flex;font-size:9px;color:#444}
.segment span{flex:1;display:flex;align-items:center;justify-content:center;gap:4px;border-right:1px solid var(--teal)}
.segment span:last-child{border-right:none}
.segment em{font-style:normal;color:var(--teal)}
.label{position:absolute;left:28px;font-size:8px;color:#888}
.value{position:absolute;font-size:8px;color:#777;font-weight:500;transform:translateX(-50%)}
.btn{position:absolute;top:275px;height:27px;border-radius:14px;display:flex;align-items:center;justify-content:center;font-size:8.5px;font-weight:500}
.btn--apply{left:23px;width:103px;background:var(--teal);color:var(--white)}
.btn--reset{left:149px;width:66px;background:#ececec;color:var(--teal)}

/* notifications */
.notify-body{position:absolute;left:0;top:63px;width:100%;height:238px;background:var(--white)}
.notify-empty{position:absolute;left:0;top:301px;width:100%;height:155px;background:var(--paper)}
.notify-title{position:absolute;left:30px;top:86px;font-size:14.5px;color:var(--teal)}
.pref{position:absolute;left:30px;width:186px;font-size:9px;color:#333}
.pref small{display:block;font-size:4.5px;color:#888;margin-top:1px}
.pref-divider{position:absolute;left:30px;width:186px;height:1px;background:#eee}
.toggle{position:absolute;left:184px;width:30px;height:16px;border-radius:8px;background:var(--teal)}
.toggle::after{content:"";position:absolute;right:2px;top:2px;width:12px;height:12px;border-radius:50%;background:var(--white)}
</style>
</head>
<body>

<!-- Splash -->
<section class="screen screen--splash">
  <div class="brand-mark splash-mark"></div>
  <div class="brand-name">PumpWatch NG</div>
</section>

<!-- Sign in -->
<section class="screen screen--signin">
  <div class="brand-mark signin-mark"></div>
  <div class="pill pill--social" style="top:181px">Linkbook</div>
  <div class="pill pill--social" style="top:222px">Searchly</div>
  <div class="or">OR</div>
  <div class="pill pill--field" style="top:286px">Email
    <svg width="12" height="9" viewBox="0 0 12 9"><rect width="12" height="9" rx="1" fill="#c8c8c8"/><path d="M0 1l6 4 6-4" stroke="#fff" fill="none"/></svg>
  </div>
  <div class="pill pill--field" style="top:327px">Password
    <svg width="8" height="10" viewBox="0 0 8 10"><rect y="4" width="8" height="6" rx="1" fill="#c8c8c8"/><path d="M2 4V3a2 2 0 014 0v1" stroke="#c8c8c8" fill="none" stroke-width="1.2"/></svg>
  </div>
  <div class="pill pill--primary" style="top:370px">SIGN IN</div>
  <div class="forgot">Forgot password?</div>
  <div class="signup">Don't have account? <b>Sign Up</b></div>
</section>

<!-- Fuel stations -->
<section class="screen screen--stations">
  <div class="map" role="img" aria-label="Street map of the area around the user"></div>
  <svg class="abs" style="left:132px;top:92px" width="80" height="80" viewBox="0 0 80 80">
    <circle cx="40" cy="40" r="40" fill="#f7e66a" opacity=".55"/>
    <circle cx="40" cy="42" r="5" fill="#f59a3a"/>
  </svg>
  <svg class="abs" style="left:158px;top:78px" width="28" height="38" viewBox="0 0 28 38">
    <path d="M14 2a12 12 0 0112 12c0 9-12 22-12 22S2 23 2 14A12 12 0 0114 2z" fill="var(--pin)"/>
    <circle cx="14" cy="14" r="6" fill="#fff"/>
  </svg>
  <header class="app-bar">
    <svg class="app-bar__menu" width="17" height="12" viewBox="0 0 17 12"><path d="M0 1h17M0 6h17M0 11h17" stroke="#fff" stroke-width="1.6"/></svg>
    <div class="app-bar__title">Fuel stations</div>
    <div class="avatar" role="img" aria-label="User profile photo"></div>
  </header>
  <div class="search">
    <svg width="14" height="14" viewBox="0 0 14 14"><circle cx="6" cy="6" r="5" stroke="#c8c8c8" fill="none" stroke-width="1.4"/><path d="M10 10l3 3" stroke="#c8c8c8" stroke-width="1.4"/></svg>
    Search station
  </div>
  <div class="filter-btn">Filter</div>
  <div class="station-card">
    <div class="station-card__head">
      <span style="left:11px">Price</span>
      <span style="left:69px">Filling Stations</span>
      <span style="left:154px">Location</span>
    </div>
    <div class="station-row"><span class="price">₦225</span><i class="dot"></i><span class="name">Okavo</span><span class="dist">800m</span></div>
    <div class="station-row"><span class="price">₦225</span><i class="dot"></i><span class="name">Tarra</span><span class="dist">850m</span></div>
    <div class="station-row"><span class="price">₦225</span><i class="dot"></i><span class="name">Cobalt</span><span class="dist">2.6Km</span></div>
    <div class="station-row"><span class="price">₦225</span><i class="dot"></i><span class="name">Asteri</span><span class="dist">900m</span></div>
    <div class="station-row"><span class="price">₦225</span><i class="dot"></i><span class="name">MKT</span><span class="dist">12Km</span></div>
    <div class="station-row"><span class="price">₦225</span><i class="dot"></i><span class="name">Raylo</span><span class="dist">2.5Km</span></div>
    <div class="station-row"><span class="price">₦225</span><i class="dot"></i><span class="name">NPX</span><span class="dist">200m</span></div>
    <div class="scrollbar"><i></i></div>
  </div>
  <nav class="tab-bar">
    <div class="tab tab--active" style="left:28px"><svg width="12" height="12" viewBox="0 0 12 12"><path d="M1.5 6L6 1.5 10.5 6v5h-9z" fill="none" stroke="currentColor"/></svg>HOME</div>
    <div class="tab" style="left:87px"><svg width="13" height="12" viewBox="0 0 13 12"><path d="M6.5 11S1 7.5 1 4a2.7 2.7 0 015.5-1A2.7 2.7 0 0112 4c0 3.5-5.5 7-5.5 7z" fill="none" stroke="currentColor"/></svg>FAVOURITES</div>
    <div class="tab" style="left:161px"><svg width="11" height="12" viewBox="0 0 11 12"><path d="M2 9V5.5a3.5 3.5 0 017 0V9l1 1H1zM4.5 11h2" fill="none" stroke="currentColor"/></svg>NOTIFICATIONS</div>
    <div class="tab" style="left:228px"><svg width="11" height="12" viewBox="0 0 11 12"><circle cx="5.5" cy="3.5" r="2.5" fill="none" stroke="currentColor"/><path d="M1 11.5a4.5 4.5 0 019 0z" fill="none" stroke="currentColor"/></svg>PROFILE</div>
  </nav>
</section>

<!-- Sort & filter sheet -->
<section class="screen screen--filter">
  <div class="dim-bar"></div>
  <div class="blur-glow"></div>
  <div class="sheet">
    <h2 style="top:23px">Sort Stations by</h2>
    <div class="segment">
      <span>PRICES <em>⇅</em></span><span>A - Z <em>⇅</em></span><span>KM <em>⇅</em></span>
    </div>
    <h2 style="top:104px">Filling Station Filter</h2>
    <div class="label" style="top:135px">Price range</div>
    <svg class="abs" style="left:28px;top:140px" width="186" height="42" viewBox="0 0 186 42">
      <g fill="#e3e3e3">
        <rect x="30" y="29" width="11" height="9"/><rect x="42" y="23" width="11" height="15"/>
        <rect x="55" y="21" width="11" height="17"/><rect x="68" y="15" width="11" height="23"/>
        <rect x="81" y="2" width="11" height="36"/><rect x="94" y="12" width="11" height="26"/>
        <rect x="107" y="17" width="11" height="21"/><rect x="120" y="19" width="11" height="19"/>
        <rect x="133" y="24" width="11" height="14"/><rect x="146" y="30" width="11" height="8"/>
        <rect x="159" y="33" width="11" height="5"/>
      </g>
      <line x1="0" y1="38" x2="186" y2="38" stroke="#ddd" stroke-width="1.5"/>
      <line x1="43" y1="38" x2="152" y2="38" stroke="var(--teal)" stroke-width="2"/>
      <circle cx="43" cy="38" r="5" fill="var(--teal)"/><circle cx="152" cy="38" r="5" fill="var(--teal)"/>
    </svg>
    <div class="value" style="left:71px;top:189px">₦182</div>
    <div class="value" style="left:180px;top:189px">₦225</div>
    <div class="label" style="top:218px">Location</div>
    <svg class="abs" style="left:28px;top:230px" width="186" height="12" viewBox="0 0 186 12">
      <line x1="0" y1="6" x2="186" y2="6" stroke="#ddd" stroke-width="1.5"/>
      <line x1="26" y1="6" x2="152" y2="6" stroke="var(--teal)" stroke-width="2"/>
      <circle cx="26" cy="6" r="5" fill="var(--teal)"/><circle cx="152" cy="6" r="5" fill="var(--teal)"/>
    </svg>
    <div class="value" style="left:54px;top:245px">50m</div>
    <div class="value" style="left:180px;top:245px">1Km</div>
    <div class="btn btn--apply">APPLY FILTERS</div>
    <div class="btn btn--reset">RESET</div>
  </div>
</section>

<!-- Notifications -->
<section class="screen screen--notify">
  <header class="app-bar">
    <svg class="app-bar__menu" width="17" height="12" viewBox="0 0 17 12"><path d="M0 1h17M0 6h17M0 11h17" stroke="#fff" stroke-width="1.6"/></svg>
    <div class="app-bar__title">Notification</div>
    <div class="avatar" role="img" aria-label="User profile photo" style="left:204px"></div>
  </header>
  <div class="notify-body"></div>
  <div class="notify-empty"></div>
  <div class="notify-title">Push Notifications</div>
  <div class="pref" style="top:121px">Price Changes</div>
  <div class="toggle" style="top:118px"></div>
  <div class="pref-divider" style="top:141px"></div>
  <div class="pref" style="top:150px">Petrol News &amp; Updates</div>
  <div class="toggle" style="top:147px"></div>
  <div class="pref-divider" style="top:170px"></div>
  <div class="pref" style="top:174px">Promos &amp; Deals<small>Get access to deals and exclusive savings</small></div>
  <div class="toggle" style="top:176px"></div>
  <nav class="tab-bar">
    <div class="tab tab--active" style="left:28px"><svg width="12" height="12" viewBox="0 0 12 12"><path d="M1.5 6L6 1.5 10.5 6v5h-9z" fill="none" stroke="currentColor"/></svg>HOME</div>
    <div class="tab" style="left:87px"><svg width="13" height="12" viewBox="0 0 13 12"><path d="M6.5 11S1 7.5 1 4a2.7 2.7 0 015.5-1A2.7 2.7 0 0112 4c0 3.5-5.5 7-5.5 7z" fill="none" stroke="currentColor"/></svg>FAVOURITES</div>
    <div class="tab" style="left:161px"><svg width="11" height="12" viewBox="0 0 11 12"><path d="M2 9V5.5a3.5 3.5 0 017 0V9l1 1H1zM4.5 11h2" fill="none" stroke="currentColor"/></svg>NOTIFICATIONS</div>
    <div class="tab" style="left:228px"><svg width="11" height="12" viewBox="0 0 11 12"><circle cx="5.5" cy="3.5" r="2.5" fill="none" stroke="currentColor"/><path d="M1 11.5a4.5 4.5 0 019 0z" fill="none" stroke="currentColor"/></svg>PROFILE</div>
  </nav>
</section>

</body>
</html>
```